Etikett für Rotweinflasche
Liebe pinselhaus Studio, wir werden uns bei der endgültigen Etikettengestaltung (finale Größe + Rückseite) noch an Euch melden. Bitte sendet uns euren Kontakt an marta.lindner@montelvo.wine
Zielgruppe
Montelvo Italia ist ein exklusives Boutique-Weingut in Sizilien, das hochqualitative Spitzenweine in kleinen Mengen mit modernster Technologie und stets nachhaltig erzeugt. Wir hinterfragen sowohl in der Agronomie im Weingarten als auch in der Önologie im Weinkeller alle herrschenden Traditionen und trachten danach, stets das beste Endprodukt zu kreieren. Der vulkanische, kalkreiche Boden Siziliens sowie trockene, sonnenreiche und niederschlagsarme Vegetationsperioden sind unsere optimale Basis.
Zielgruppe: Internationale Genussmenschen jeglichen Alters, die sich bewusst auch höherpreisige Weine (um die €30+) gönnen , vor allem kunstaffine young professionals mit Qualitäts-& Nachhaltigkeitsanspruch
Aufgabenstellung
Das Etikett ist für Rotwein-Flaschen (Cabernet Sauvignon / Nero D'Avola / Frappato / Syrah / Cerasuolo / Petit Verdot / sowie einen Bourdeaux-Cuveè aus Cabernet Sauvignon und Petit Verdot) .
Die Flasche ist reinschwarz, sehr hochwertig und schwer.
Flaschenform: Bordeauxflasche siehe technisches Datenblatt
Sleeve über dem Korken: schwarz mit weißer Schrift wie bisher
Zu gestalten ist das Etikett der Vorderseite. Zumindest die jeweilige Rotwein-Sorte ist auch textlich darzustellen (zwecks Scannen mit Traubly-App)
Der Kreativität kann freien Lauf gelassen werden! Unterscheidbarkeit vom Markt ist explizit gewollt.
Unsere aktuellen Etiketten und Markenauftritt siehe: https://montelvo.wine/shop/

```html
<!DOCTYPE html>
<html lang="de">
<head>
<meta charset="utf-8">
<title>Montelvo Italia – Cabernet Sauvignon Etikett</title>
<link rel="stylesheet" href="https://fonts.googleapis.com/css2?family=Barlow:wght@300;600;700&family=League+Spartan:wght@700&display=swap">
<style>
  :root {
    --frame: #757575;
    --paper: #ffffff;
    --ink: #0d0d0d;
    --sketch-light: #f4f4f4;
    --sketch-mid: #c9c9c9;
    --sketch-dark: #8a8a8a;
  }
  html, body {
    margin: 0;
    padding: 0;
    width: 1200px;
    height: 800px;
    overflow: hidden;
    background: var(--frame);
  }
  .label {
    position: relative;
    width: 1200px;
    height: 800px;
    background: var(--frame);
  }
  .label-face {
    position: absolute;
    left: 38px;
    top: 38px;
    width: 1124px;
    height: 724px;
    background: var(--paper);
    overflow: hidden;
  }
  .winery {
    position: absolute;
    left: 32px;
    top: 47px;
    margin: 0;
    font-family: "Barlow", sans-serif;
    font-weight: 700;
    font-size: 44px;
    line-height: 48px;
    letter-spacing: 0.11em;
    color: var(--ink);
    white-space: nowrap;
  }
  .varietal {
    position: absolute;
    left: 28px;
    top: 183px;
    margin: 0;
    font-family: "League Spartan", sans-serif;
    font-weight: 700;
    font-size: 121px;
    line-height: 113px;
    letter-spacing: -0.01em;
    color: var(--ink);
    white-space: nowrap;
  }
  .varietal span { display: block; }
  .region {
    position: absolute;
    left: 32px;
    top: 541px;
    margin: 0;
    font-family: "Barlow", sans-serif;
    font-weight: 700;
    font-size: 47px;
    line-height: 52px;
    letter-spacing: 0.09em;
    color: var(--ink);
  }
  .vintage {
    position: absolute;
    left: 32px;
    top: 629px;
    margin: 0;
    font-family: "Barlow", sans-serif;
    font-weight: 300;
    font-size: 35px;
    line-height: 40px;
    letter-spacing: 0.08em;
    color: var(--ink);
  }
  .landscape {
    position: absolute;
    left: 742px;
    top: 42px;
    width: 340px;
    height: 543px;
    background: linear-gradient(180deg, var(--sketch-light) 0%, var(--sketch-light) 25%, var(--sketch-mid) 60%, var(--sketch-dark) 100%);
  }
</style>
</head>
<body>
  <main class="label">
    <section class="label-face">
      <p class="winery">MONTELVO ITALIA</p>
      <h1 class="varietal"><span>CABERNET</span><span>SAUVIGNON</span></h1>
      <p class="region">SIZILIEN</p>
      <p class="vintage">2022</p>
      <div class="landscape" role="img" aria-label="Bleistiftzeichnung eines sizilianischen Felsbergs mit Bergdorf an seinem Fuß"></div>
    </section>
  </main>
</body>
</html>
```